Startup incubator requires a funky cool brochure

please see design brief, please be creative but within the design confines listed in the corporatedesign pdf file

Startup

```html
<!DOCTYPE html>
<html lang="en">
<head>
<meta charset="utf-8">
<title>Launchbay Brochure</title>
<link rel="stylesheet" href="https://fonts.googleapis.com/css2?family=Cinzel:wght@400&family=Open+Sans:ital,wght@0,400;0,600;1,400&family=Raleway:wght@300;400&display=swap">
<style>
  :root {
    --orange: #f2a81d;
    --charcoal: #3b3b3d;
    --charcoal-deep: #2c2c2e;
    --ink: #4a4a4a;
    --paper: #ffffff;
    --backdrop: #6a6a6a;
    --callout-grey: #6a6a6a;
    --fee-text: #f0f0f0;
  }
  * { box-sizing: border-box; margin: 0; padding: 0; }
  html, body { width: 1200px; height: 900px; overflow: hidden; }
  body { background: var(--backdrop); font-family: "Open Sans", sans-serif; color: var(--ink); position: relative; }

  .spread { position: absolute; display: flex; box-shadow: 0 6px 18px rgba(0,0,0,.35); }
  .spread--location { left: 80px; top: 25px; }
  .spread--letter { left: 526px; top: 455px; }

  .page { width: 297px; height: 420px; position: relative; overflow: hidden; }
  .page--white { background: var(--paper); }
  .page--orange { background: var(--orange); }
  .page--cover { background: linear-gradient(160deg, #4d4d4f 0%, var(--charcoal-deep) 100%); }

  .footer-band { position: absolute; left: 0; right: 0; bottom: 0; background: var(--charcoal); }
  .page-number { position: absolute; bottom: 10px; font-size: 6px; color: var(--orange); }

  .brand { position: absolute; top: 28px; left: 0; right: 0; display: flex; justify-content: center; align-items: center; gap: 4px;
           font-family: "Open Sans", sans-serif; font-weight: 600; font-size: 9px; letter-spacing: 2px; }
  .brand__mark { width: 6px; height: 6px; background: currentColor; }
  .brand--orange { color: var(--orange); }
  .brand--white { color: #f2f2f2; }
  .brand--dark { color: var(--charcoal); }

  .heading { font-family: "Cinzel", serif; font-weight: 400; letter-spacing: 1px; }
  .body-text { font-size: 5.3px; line-height: 1.5; }
  .body-text p + p { margin-top: 6px; }

  /* Location page */
  .location__heading { position: absolute; left: 30px; top: 140px; font-size: 15px; color: var(--orange); }
  .location__address { position: absolute; left: 30px; top: 160px; font-family: "Raleway", sans-serif; font-size: 8px; letter-spacing: .8px; color: var(--ink); }
  .location__body { position: absolute; left: 30px; top: 185px; width: 150px; }

  /* Letter page */
  .letter__heading { position: absolute; left: 70px; top: 100px; font-size: 13px; color: #fff; letter-spacing: 1.5px; }
  .letter__body { position: absolute; left: 70px; top: 125px; width: 205px; font-style: italic; font-size: 4.9px; line-height: 1.45; color: #3a2b10; }
  .letter__body p + p { margin-top: 5px; }

  /* Services page */
  .services__photo { position: absolute; right: 0; top: 10px; width: 150px; height: 108px; background: linear-gradient(135deg, #d9d9d9 0%, #8f8f8f 60%, #2d2d2d 100%); }
  .services__heading { position: absolute; left: 22px; top: 128px; font-size: 13px; color: var(--orange); }
  .services__col { position: absolute; top: 150px; width: 122px; font-size: 4.6px; line-height: 1.4; }
  .services__col p + p { margin-top: 5px; }
  .services__col--left { left: 22px; }
  .services__col--right { left: 156px; }
  .services__list { list-style: none; border-left: 1px solid var(--orange); padding-left: 4px; margin-top: 5px; }
  .services__list li { position: relative; padding-left: 6px; }
  .services__list li + li { margin-top: 2.5px; }
  .services__list li::before { content: ""; position: absolute; left: 0; top: 2.2px; width: 2.3px; height: 2.3px; background: var(--ink); }
  .services__col .services__callout { margin-top: 7px; font-family: "Raleway", sans-serif; font-weight: 300; font-size: 7px; line-height: 1.15; color: var(--callout-grey); text-transform: uppercase; }
  .services__band { height: 60px; }
  .services__fees { position: absolute; bottom: 14px; left: 22px; right: 22px; display: flex; gap: 16px; color: var(--fee-text); font-size: 4.8px; line-height: 1.5; }
  .services__fees p { flex: 1; }
</style>
</head>
<body>

  <section class="spread spread--location">
    <article class="page page--white">
      <div class="brand brand--orange"><span class="brand__mark"></span>LAUNCHBAY</div>
      <h2 class="heading location__heading">Location:</h2>
      <p class="location__address">LINDENALLEE 12, 40213</p>
      <div class="body-text location__body">
        <p>Our ideal facility is located in the heart of Dusseldorf on Lindenallee, close to the Kronenallee the most exclusive shopping street in Germany and within easy reach of Weidenstrasse, the highest grossing shopping street in Germany, in other words, we have prime retail space, and we're offering it to you for free!</p>
        <p>We are currently offering 800qm of space, and seeking to share this area out amongst a limited number companies once we are fully operational including 1-2 café/bar/restaurant area(s) which will help keep you and your customers energized throughout the day.</p>
        <p>You can find a variety of transportation options within 100m of our front door including the U-bahn station, tram stops for the 707, and bus stations for providing your customers with easy access to your offerings.</p>
      </div>
      <div class="footer-band" style="height:75px"></div>
      <span class="page-number" style="left:30px">3</span>
    </article>
    <article class="page page--cover">
      <div class="brand brand--white"><span class="brand__mark"></span>LAUNCHBAY</div>
    </article>
  </section>

  <section class="spread spread--letter">
    <article class="page page--orange">
      <div class="brand brand--dark"><span class="brand__mark"></span>LAUNCHBAY</div>
      <h2 class="heading letter__heading">Opening Letter</h2>
      <div class="letter__body">
        <p>Starting Your Own Business Can Be Tough, There Are Challenges That Are Unforeseen, Limitations That You May Not Have Expected And Difficulties That You May Struggle To Face Alone. In This Delicate And Stressful Time Having The Right Partner Can Be Crucial To Your Success, And At Launchbay We Strive To Be That Partner, Helping Start-ups Through The Toughest Time Of Their Lives And Helping Them Mature Into Robust And Successful Businesses.</p>
        <p>Three Young Entrepreneurs, Much Like Yourself, Realized That Young Businesses Did Not Have The Support Or Space Which Would Otherwise Have Allowed Them To Succeed And Be Profitable. Samir Haddad And Brothers Leon &amp; Jonas Brandt Decided To Create A Business With The Aim Of Optimizing Start-ups Prospects Of Success, A Space That Would Have Been Instrumental In Helping Them With Their Own Businesses.</p>
        <p>Samir, Currently A Business Developer With Nordwerk Here In Dusseldorf, Maintains A Facility Management Business In The U.A.E, Whilst Jonas (Our Gm) Co-founded K.R.T With His Brother Leon (Himself A 3 Year Veteran Of Baufeld GmbH – A Commercial And Residential Property Development Company In Dusseldorf), A Company Which Focuses On Property Development In Nrw.</p>
        <p>Launchbay Is An Incubator (Business Development) Service In Dusseldorf, Combining Free Operating Space And Professional Consultancy Services Specifically Designed To Nurture Young Businesses. Business Plans For Retail Companies Generally Require A Cost Designation Of 20% Of Annual Sales To Be Set Aside For Commercial Rental Costs, By Removing This Requirement And Providing Our Numerous Additional Services We Tangibly Reduce Your Risk And Give You A Helping Hand On Your Way To Establishing A Successful And Sustainable Business</p>
        <p>Our Vision Is To Promote Innovative Entrepreneurism In Dusseldorf By Discovering Interesting Businesses And Offering Them Services And Space On A No Rent/no Deposit Basis In Return For Remuneration Directly Based On Sales, With No Base Fees Or Hidden Costs. Our Journey Will Develop A Highly Networked Community Of Likeminded Entrepreneurs Operating In One Space And Offering Advice And Examples To Each Other In A Safer And Protected Environment.</p>
        <p>We Believe That Our Business Will Become A Strong Asset For Our Partners In The Growing Entrepreneurial Community In This City And We Cannot Wait To Share Our Ideas With You!</p>
        <p>Best Regards,</p>
      </div>
      <div class="footer-band" style="height:50px"></div>
      <span class="page-number" style="left:30px">1</span>
    </article>

    <article class="page page--white">
      <div class="services__photo" role="img" aria-label="Photograph of a person in a dark suit and bow tie with sketched business ideas in place of the head"></div>
      <h2 class="heading services__heading">Services</h2>
      <div class="services__col services__col--left">
        <p>Launchbay Dusseldorf is prepared to provide your business with solutions that will mitigate the majority of overhead costs and initial investment costs that would normally be required to establish a retail business.</p>
        <p>Upon entering into an arrangement with us, we are committed to providing you with:</p>
        <ul class="services__list">
          <li>Shop/Display/Operating Space in a super-central, fashionable, high footfall location</li>
          <li>No Utility Costs (incl. gas, water, electricity and WiFi)</li>
          <li>Professional Meeting Rooms and Well Equipped Workspaces for Backroom Administration</li>
          <li>A communal ERP System with individualized accounts and settings.</li>
          <li>Business Development Advice (in-house)</li>
          <li>Free Seminars/Tutoring for various business administration skills from qualified professional staff (outsourced)</li>
          <li>A communal location attracting a wide range of otherwise unexposed customers</li>
        </ul>
      </div>
      <div class="services__col services__col--right">
        <p>Our goal is to help your business prove its concept, helping you to earn enough investment capital to establish your own stand-alone location, although if you want to stay for a while, we can certainly discuss it.</p>
        <p>The challenges in proving your concept can be daunting, sleepless nights watching your lifesavings are sunk into an unproven business or worse, feeling the weight of the repayments on the investment/start-up loans.</p>
        <p>The opportunity to determine whether your business is feasible in the marketplace with ZERO financial risk while at the same time earning the same margins and profits than you would in your very own store is an opportunity that sells itself.</p>
        <p>Whenever you feel comfortable 'leaving the nest' you will be in a much more confident position with your endeavor, and</p>
        <p class="services__callout">The banks will certainly appreciate your proven concept when it comes determining your business' credit-worthiness!</p>
      </div>
      <div class="footer-band services__band"></div>
      <div class="services__fees">
        <p>Our all-inclusive remuneration will ultimately depend on the revenue you can generate. Launchbay will take a 15% service charge for the first $15,000 in sales per month. Should the business generate</p>
        <p>$15,000-$20,000 the service charge will drop to 10%, and any sales above $20,000 will only incur a 7.5% charge.</p>
      </div>
      <span class="page-number" style="right:22px">2</span>
    </article>
  </section>

</body>
</html>
```